VALMIKE GROUP

This is a company that provides executive protection. Our motto is "New Era in Protection"... I don't want this to look like other security websites. I want it to be clean and sharp and represent a new era. We are based in the bay area so maybe a picture of San Francisco in the background?
I want it to be able to funnel down a couple different categories.
1. About Us
2. Services (Executive Protection, Covert Protection, Residential Protection & Intelligence)
3. Iron Finch (Training & Consulting)
4. Contact Us
I want it to be very clean and modern. I don't want there to be any pictures of bodyguards with ear pieces like every other website.
Target Market(s)
Ultra High Net Worth Individuals
Coding
Coded - Design and coding required
Number of Pages Required
1 page
Requirements
Must have
- Colors of my Symbol
Nice to have
- City in the background, San Francisco, New York or the Pinehallow Club in Montana.
Should not have
- Should not look like an KVM website or have photos of bodyguards. I want this to be a clean and simple website with my logo

```html
<!DOCTYPE html>
<html lang="en">
<head>
<meta charset="utf-8">
<title>Valmike Group — New Era in Protection</title>
<link href="https://fonts.googleapis.com/css2?family=Lato:wght@400;700;900&display=swap" rel="stylesheet">
<style>
:root{
  --brand:#7a0d14;
  --ink:#111;
  --text:#444;
  --soft:#f4f4f4;
  --white:#fff;
  --footer:#000;
  --muted:#bdbdbd;
}
*{box-sizing:border-box;margin:0;padding:0}
html,body{width:1200px;height:3475px;overflow:hidden}
body{font-family:'Lato',sans-serif;color:var(--text);background:var(--white);position:relative}
a{color:inherit;text-decoration:none}

.site-header{position:absolute;top:0;left:0;width:1200px;height:88px;background:var(--white)}
.brand{position:absolute;left:75px;top:18px;display:flex;align-items:center;gap:10px}
.brand-mark{width:34px;height:34px;background:var(--brand)}
.brand-name{font-weight:900;font-size:20px;letter-spacing:1px;color:var(--ink);line-height:1}
.main-nav{position:absolute;right:74px;top:38px;display:flex;gap:36px;font-size:14px;font-weight:700;color:var(--ink)}
.main-nav .active{color:var(--brand)}

.hero{position:absolute;top:88px;left:0;width:1200px;height:671px;
  background:linear-gradient(180deg,#3c4660 0%,#55607a 30%,#2a3042 55%,#3a3530 75%,#1b2230 100%);text-align:center;color:var(--white)}
.hero-title{position:absolute;top:262px;width:100%;font-size:82px;font-weight:900;letter-spacing:1px}
.hero-tagline{position:absolute;top:355px;width:100%;font-size:38px;font-weight:700}
.hero-dots{position:absolute;top:617px;left:568px;display:flex;gap:8px}
.hero-dots span{width:9px;height:9px;border-radius:50%;background:rgba(255,255,255,.5)}
.hero-dots span:first-child{background:var(--white)}

.btn{display:inline-block;background:var(--brand);color:var(--white);font-weight:700;font-size:15px;
  width:180px;height:51px;line-height:51px;text-align:center;border-radius:5px}

.about{position:absolute;top:759px;left:0;width:1200px;height:553px}
.about-mark{position:absolute;left:75px;top:65px;width:393px;height:417px;display:flex;flex-direction:column;align-items:center;justify-content:center;gap:26px}
.about-mark .square{width:200px;height:200px;background:var(--brand)}
.about-mark .name{font-size:40px;font-weight:900;color:var(--brand);letter-spacing:1px}
.about-copy{position:absolute;left:524px;top:84px;width:570px}
.about-copy h2{font-size:41px;font-weight:900;color:var(--ink);line-height:43px;padding-left:4px}
.about-copy h2 span{color:var(--brand)}
.about-copy p{margin-top:22px;font-size:17px;line-height:30.5px}
.about-copy .btn{margin-top:36px}

.service{position:absolute;left:0;width:1200px;height:391px;overflow:hidden}
.service.alt{background:var(--soft)}
.service .photo{position:absolute;top:0;height:391px}
.service .copy{position:absolute;width:485px}
.service h3{font-size:30px;font-weight:900;color:var(--ink);line-height:31px}
.service p{margin-top:20px;font-size:14.5px;line-height:27.5px}
.service .btn{margin-top:34px}

.exec{top:1312px}
.exec .photo{left:576px;width:624px;clip-path:polygon(44px 0,100% 0,100% 100%,0 100%);
  background:linear-gradient(120deg,#d8d6d2,#8f8b86 45%,#c9c3bb 70%,#e7e4df)}
.exec .copy{left:75px;top:72px}
.covert{top:1702px}
.covert .photo{left:0;width:624px;clip-path:polygon(0 0,576px 0,100% 100%,0 100%);
  background:linear-gradient(135deg,#1c2a44,#0d1a36 40%,#1d4aa0 70%,#0b1430)}
.covert .copy{left:645px;top:72px}
.resi{top:2093px}
.resi .photo{left:576px;width:624px;clip-path:polygon(48px 0,100% 0,100% 100%,0 100%);
  background:linear-gradient(120deg,#b7c6de,#e8edf4 45%,#d8b49b 70%,#a27256)}
.resi .copy{left:75px;top:63px}

.iron-finch{position:absolute;top:2484px;left:0;width:1200px;height:594px}
.iron-finch h2{position:absolute;top:60px;width:100%;text-align:center;font-size:38px;font-weight:900;color:var(--ink)}
.iron-finch .intro{position:absolute;top:122px;left:75px;width:1050px;text-align:center;font-size:17px;line-height:30.5px}
.iron-finch .photo{position:absolute;left:75px;top:213px;width:512px;height:313px;
  background:linear-gradient(110deg,#eef0f0,#d9dbdc 40%,#9aa3aa 70%,#c9cdd0)}
.iron-finch .copy{position:absolute;left:625px;top:254px;width:490px}
.iron-finch h3{font-size:29px;font-weight:900;color:var(--brand)}
.iron-finch p{margin-top:18px;font-size:14.5px;line-height:27.5px}
.iron-finch .btn{margin-top:32px}

.site-footer{position:absolute;top:3130px;left:0;width:1200px;height:345px;background:var(--footer);color:var(--muted)}
.newsletter{position:absolute;top:3078px;left:75px;width:1051px;height:104px;background:var(--brand);z-index:2}
.newsletter h4{position:absolute;left:85px;top:30px;font-size:33px;font-weight:400;color:var(--white)}
.newsletter .field{position:absolute;left:391px;top:28px;width:389px;height:48px;background:var(--white);
  font-size:13px;font-weight:700;color:#333;line-height:48px;padding-left:14px}
.newsletter .submit{position:absolute;left:790px;top:28px;width:170px;height:48px;background:var(--footer);
  color:var(--white);font-size:18px;font-weight:700;line-height:48px;text-align:center}

.footer-brand{position:absolute;left:75px;top:130px}
.footer-brand .brand-row{display:flex;align-items:center;gap:10px}
.footer-brand .brand-row .sq{width:46px;height:46px;background:var(--white)}
.footer-brand .brand-row span{font-size:24px;font-weight:900;color:var(--white);letter-spacing:1px}
.footer-brand .legal{margin-top:30px;font-size:13px;line-height:20px;color:var(--white)}
.socials{display:flex;gap:18px;margin-top:22px}
.socials span{width:20px;height:20px;border-radius:50%;background:var(--white)}
.footer-col{position:absolute;top:117px}
.footer-col h5{font-size:19px;font-weight:400;color:var(--white);margin-bottom:10px}
.footer-col li{list-style:none;font-size:14px;line-height:31.5px}
.col-links{left:341px}
.col-services{left:568px}
.col-contact{left:885px;width:220px}
.col-contact p{font-size:14px;line-height:23px}
.contact-line{display:flex;align-items:center;gap:18px;font-size:14px;margin-top:12px}
.contact-line svg{width:14px;height:14px;fill:var(--muted)}
</style>
</head>
<body>

<header class="site-header">
  <a class="brand" href="#"><span class="brand-mark"></span><span class="brand-name">VALMIKE GROUP</span></a>
  <nav class="main-nav">
    <a class="active" href="#">HOME</a>
    <a href="#">ABOUT US</a>
    <a href="#">SERVICES</a>
    <a href="#">IRON FINCH</a>
    <a href="#">CONTACT US</a>
  </nav>
</header>

<section class="hero" role="img" aria-label="San Francisco skyline and Bay Bridge at dusk">
  <h1 class="hero-title">VALMIKE GROUP</h1>
  <p class="hero-tagline">NEW ERA IN PROTECTION</p>
  <div class="hero-dots"><span></span><span></span><span></span><span></span></div>
</section>

<section class="about">
  <div class="about-mark"><span class="square"></span><span class="name">VALMIKE GROUP</span></div>
  <div class="about-copy">
    <h2>ABOUT<br><span>VALMIKE GROUP</span></h2>
    <p>Sed in nunc lorem. Sed luctus hendrerit facilisis sit amet enim quis nibh ultricies&nbsp; convallis. Aliquam egestas dapibus odio ut lobortis mattis nisi, in convallis enim.&nbsp; Proin a diam et diam efficitur ultricies nec eget tellus.<br>&nbsp;Proin ultricies purus sed dui&nbsp; efficitur rutrum. Nulla viverra purus a sapien varius, a posuere lectus tristique. Sed hendrerit eleifend odio,<br>non pulvinar sapien ullamcorper sed.</p>
    <a class="btn" href="#">READ MORE</a>
  </div>
</section>

<section class="service alt exec">
  <div class="photo" role="img" aria-label="Executives meeting in a bright modern lounge"></div>
  <div class="copy">
    <h3>EXECUTIVE PROTECTION</h3>
    <p>Sed in nunc lorem. Sed luctus hendrerit facilisis sit amet enim quis nibh ultricies convallis. Aliquam egestas dapibus odio ut lobortis mattis nisi, in convallis enim. Proin a diam et diam efficitur ultricies nec eget tellus. Proin ultricies purus sed dui efficitur rutrum</p>
    <a class="btn" href="#">READ MORE</a>
  </div>
</section>

<section class="service covert">
  <div class="photo" role="img" aria-label="Team gathered around a glowing blue digital table"></div>
  <div class="copy">
    <h3>COVERT PROTECTION</h3>
    <p>Sed in nunc lorem. Sed luctus hendrerit facilisis sit amet enim quis nibh ultricies convallis. Aliquam egestas dapibus odio ut lobortis mattis nisi, in convallis enim. Proin a diam et diam efficitur ultricies nec eget tellus. Proin ultricies purus sed dui efficitur rutrum</p>
    <a class="btn" href="#">READ MORE</a>
  </div>
</section>

<section class="service alt resi">
  <div class="photo" role="img" aria-label="Hands sheltering a small white model house"></div>
  <div class="copy">
    <h3>RESIDENTIAL PROTECTION<br>&amp; INTELLIGENCE</h3>
    <p>Sed in nunc lorem. Sed luctus hendrerit facilisis sit amet enim quis nibh ultricies convallis. Aliquam egestas dapibus odio ut lobortis mattis nisi, in convallis enim. Proin a diam et diam efficitur ultricies nec eget tellus. Proin ultricies purus sed dui efficitur rutrum</p>
    <a class="btn" href="#">READ MORE</a>
  </div>
</section>

<section class="iron-finch">
  <h2>IRON FINCH</h2>
  <p class="intro">Sed in nunc lorem. Sed luctus hendrerit facilisis sit amet enim quis nibh&nbsp; ultricies&nbsp; convallis. Aliquam egestas dapibus odio ut lobortis mattis nisi, in&nbsp; convallis enim diam et diam efficitur ultricies nec eget tellus.</p>
  <div class="photo" role="img" aria-label="Trainer presenting at a whiteboard to a small group"></div>
  <div class="copy">
    <h3>TRAINING &amp; CONSULTING</h3>
    <p>Sed in nunc lorem. Sed luctus hendrerit facilisis sit amet enim quis nibh ultricies convallis. Aliquam egestas dapibus odio ut lobortis mattis nisi, in convallis enim. Proin a diam et diam efficitur ultricies nec eget tellus. Proin ultricies purus sed dui efficitur rutrum</p>
    <a class="btn" href="#">READ MORE</a>
  </div>
</section>

<div class="newsletter">
  <h4>Newsletter Sign Up</h4>
  <div class="field">Enter Email Address</div>
  <div class="submit">Subscribe Now</div>
</div>

<footer class="site-footer">
  <div class="footer-brand">
    <div class="brand-row"><span class="sq"></span><span>VALMIKE GROUP</span></div>
    <p class="legal">Copyright © 2021 Valmike Group<br>All Rights Reserved</p>
    <div class="socials" aria-label="Social media links"><span></span><span></span><span></span><span></span><span></span></div>
  </div>
  <div class="footer-col col-links">
    <h5>Quick Links</h5>
    <ul><li>Home</li><li>About us</li><li>Services</li><li>Iron Finch</li><li>Contact</li></ul>
  </div>
  <div class="footer-col col-services">
    <h5>Services</h5>
    <ul><li>Executive Protection</li><li>Covert Protection</li><li>Residential Protection &amp; Intelligence</li></ul>
  </div>
  <div class="footer-col col-contact">
    <h5>Contact Info</h5>
    <p>2180 - 45 Harbor Lane<br>Nullam sit amet sapien<br>sollicitudin</p>
    <div class="contact-line"><svg viewBox="0 0 24 24"><path d="M6.6 10.8a15.1 15.1 0 0 0 6.6 6.6l2.2-2.2c.3-.3.7-.4 1-.2 1.1.4 2.3.6 3.6.6.6 0 1 .4 1 1V20c0 .6-.4 1-1 1A17 17 0 0 1 3 4c0-.6.4-1 1-1h3.5c.6 0 1 .4 1 1 0 1.3.2 2.5.6 3.6.1.3 0 .7-.2 1z"/></svg>1-800-555-0142</div>
    <div class="contact-line"><svg viewBox="0 0 24 24"><path d="M2 5h20v14H2z M2 5l10 8 10-8" fill="none" stroke="#bdbdbd" stroke-width="2"/></svg>hello@valmikegroup.com</div>
  </div>
</footer>

</body>
</html>
```